An internal sign in a physiotherapy clinic with gym. About working hard

We are a physiotherapy clinic / gym and we are wanting an internal wall to be a large sign with a great slogan
We are after 3 parts to it
1. The image / backdrop
2. The slogan
3. Our clinic logo

I have attached some images of the concept of what we are after. It can be climbing a mountain, rockclimbing and even hard work in a gym.

The slogan is:
"IF IT DOESN'T CHALLENGE YOU, IT WON'T CHANGE YOU"

Logo
I have attached a few different versions of our logo to assist you in the sign based on the background

THE SIGN SIZE WILL BE:
2935mm wide x 1885mm high

```html
<!DOCTYPE html>
<html lang="en">
<head>
<meta charset="utf-8">
<title>Northvale Sports Medicine – Wall Sign</title>
<link rel="stylesheet" href="https://fonts.googleapis.com/css2?family=Oswald:wght@500;600&display=swap">
<style>
  :root {
    --page-bg: #e4e4e4;
    --navy: #151c48;
    --deep-blue: #0a7fc6;
    --bright-blue: #06aee4;
    --sky: #b3e4f4;
    --white: #ffffff;
    --accent: #3fc3f0;
  }
  * { margin: 0; padding: 0; box-sizing: border-box; }
  html, body {
    width: 1200px;
    height: 1000px;
    overflow: hidden;
    background: var(--page-bg);
  }
  .wall-sign {
    position: absolute;
    left: 39px;
    top: 140px;
    width: 1123px;
    height: 720px;
    overflow: hidden;
    font-family: "Oswald", "Arial Narrow", sans-serif;
  }
  .backdrop {
    position: absolute;
    inset: 0;
    background:
      radial-gradient(ellipse 62% 75% at 18% 22%, var(--navy) 0%, var(--navy) 45%, rgba(21,28,72,0) 72%),
      linear-gradient(200deg, var(--deep-blue) 0%, var(--bright-blue) 45%, var(--sky) 100%);
  }
  .brand {
    position: absolute;
    left: 68px;
    top: 48px;
    display: flex;
    align-items: center;
    gap: 16px;
    color: var(--white);
    font-weight: 600;
  }
  .brand-dot {
    width: 26px;
    height: 26px;
    border-radius: 50%;
    background: var(--accent);
  }
  .brand-name {
    display: flex;
    flex-direction: column;
    line-height: 1;
  }
  .brand-name .primary {
    font-size: 40px;
    letter-spacing: 1px;
  }
  .brand-name .secondary {
    font-size: 15px;
    letter-spacing: 6px;
    margin-top: 6px;
  }
  .slogan {
    position: absolute;
    right: 70px;
    top: 392px;
    text-align: right;
    color: var(--white);
    font-weight: 500;
    font-size: 60px;
    line-height: 60px;
    text-transform: uppercase;
    text-shadow: 4px 6px 8px rgba(10, 40, 80, 0.35);
  }
  .slogan span { display: block; }
</style>
</head>
<body>
  <section class="wall-sign">
    <div class="backdrop" role="img" aria-label="Navy silhouette of a rock climber hanging from a rope beside a dark cliff face, against a blue sky gradient"></div>

    <div class="brand">
      <span class="brand-dot"></span>
      <div class="brand-name">
        <span class="primary">NORTHVALE</span>
        <span class="secondary">SPORTS MEDICINE</span>
      </div>
    </div>

    <h1 class="slogan">
      <span>If it doesn’t</span>
      <span>challenge you</span>
      <span>it won’t</span>
      <span>change you</span>
    </h1>
  </section>
</body>
</html>
```